"KTR Community Supports" Business Card Design

We are a not for profit disability service that has recently changed its logo and trading name and is in the process of "rebranding".We provide employment, training and accommodation to people with disabilities. We find our new logo fresh and inspiring and would like our new business cards to reflect the same feeling. Our marketing line is "Growth, Opportunity, Empowerment".

Target Market(s)

People with disabilities and their families, carers, support network

Industry/Entity Type

Business

Contact Information for Business Card

Requirements
Must have
• Our logo; space for the above listed information requirements

```html
<!DOCTYPE html>
<html lang="en">
<head>
<meta charset="utf-8">
<title>KTR Community Supports – Business Card</title>
<link href="https://fonts.googleapis.com/css2?family=Open+Sans:wght@400;600;700&display=swap" rel="stylesheet">
<style>
  :root {
    --stage: #e9e6e1;
    --card-white: #ffffff;
    --brand-blue: #1f67b1;
    --ink: #1d1d1d;
    --leaf-green: #5f9a2f;
    --green-light: #8ebf3a;
    --green-dark: #2f5e22;
    --on-green: #ffffff;
  }
  * { margin: 0; padding: 0; box-sizing: border-box; }
  html, body { width: 1200px; height: 1000px; overflow: hidden; }
  body {
    background: var(--stage);
    font-family: "Open Sans", Arial, sans-serif;
    position: relative;
  }
  .card {
    position: absolute;
    left: 265px;
    width: 665px;
    height: 397px;
    box-shadow: 0 4px 14px rgba(0,0,0,0.25);
  }
  .card-front { top: 73px; background: var(--card-white); }
  .card-back {
    top: 532px;
    background: radial-gradient(ellipse at 50% 45%, var(--green-light) 0%, var(--leaf-green) 45%, var(--green-dark) 100%);
    display: flex;
    align-items: center;
    justify-content: center;
  }
  .brand-front {
    position: absolute;
    left: 30px;
    top: 110px;
    width: 280px;
    display: flex;
    align-items: center;
    gap: 16px;
  }
  .brand-dot {
    flex: none;
    width: 54px;
    height: 54px;
    border-radius: 50%;
    background: var(--leaf-green);
  }
  .brand-name {
    font-weight: 700;
    font-size: 30px;
    line-height: 1.15;
    color: var(--leaf-green);
  }
  .contact {
    position: absolute;
    left: 390px;
    top: 106px;
    color: var(--ink);
    font-size: 15px;
    line-height: 19px;
  }
  .contact-name { font-size: 17px; font-weight: 700; color: var(--brand-blue); }
  .contact-address { margin-top: 20px; }
  .contact-lines { margin-top: 12px; list-style: none; }
  .contact-lines li { display: flex; align-items: center; gap: 6px; }
  .contact-lines svg { width: 12px; height: 12px; fill: var(--brand-blue); flex: none; }
  .brand-back {
    display: flex;
    align-items: center;
    gap: 22px;
    color: var(--on-green);
  }
  .brand-back .brand-dot { width: 110px; height: 110px; background: var(--on-green); }
  .brand-back .brand-name { color: var(--on-green); font-size: 46px; font-weight: 400; }
</style>
</head>
<body>
  <section class="card card-front">
    <div class="brand-front">
      <span class="brand-dot"></span>
      <span class="brand-name">KTR Community Supports</span>
    </div>
    <div class="contact">
      <p class="contact-name">Daniel Hartwell</p>
      <p class="contact-title">Marketing Manager</p>
      <p class="contact-address">14 Wattlebrook Road<br>Greenvale VIC 3059</p>
      <ul class="contact-lines">
        <li><svg viewBox="0 0 12 12"><path d="M2 1h3l1 3-2 1a7 7 0 0 0 3 3l1-2 3 1v3c-6 0-9-3-9-9z"/></svg>999 999 9999</li>
        <li><svg viewBox="0 0 12 12"><path d="M1 4c2-3 8-3 10 0v1H8V4H4v1H1zM3 6h6l1 5H2z"/></svg>999 999 9999</li>
        <li><svg viewBox="0 0 12 12"><path d="M3 1h6v3H3zM1 5h10v4H9v2H3V9H1z"/></svg>999 999 9999</li>
        <li><svg viewBox="0 0 12 12"><path d="M1 2h10v8H1zM2 3l4 3 4-3v1L6 7 2 4z" fill-rule="evenodd"/></svg>info@ktrcomsppt.com</li>
        <li><svg viewBox="0 0 12 12"><circle cx="6" cy="6" r="5"/></svg>www.ktrcomsppt.com</li>
      </ul>
    </div>
  </section>

  <section class="card card-back">
    <div class="brand-back">
      <span class="brand-dot"></span>
      <span class="brand-name">KTR Community<br>Supports</span>
    </div>
  </section>
</body>
</html>
```